Movie Poster/DVD jacket for Short Documentary

I am a documentary filmmaker who just completed a project titled "Cousin Marigold". Here is the logline (short description of the movie): "An Oklahoma family is ripped apart after their 15-year-old son brutally murders his older sister in 1974. Controversy swirls around the case after his parents decide to hire a prominent defense attorney to keep him out of jail." I have several good photos of the family involved. I am in the process of submitting the film to several festivals and I want a professional looking movie poster that can be sent with film submissions. The look needs to dramatic and serious.
Updates

Project Deadline Extended Reason: We just had several more submission enter today and need a few more days to evaluate. Thank you for you patience. Added Thursday, November 19, 2015

Target Market(s)

Film festivals, television

Industry/Entity Type

Movie

Colors
f04a50

Requirements
Must have
• the color red and have a similar appearance to the sample movie posters.
• Also, tagline: turning a blind eye into broken hearts
• Directors name: a film by Gus Pellam
Nice to have
• rough
Should not have
• Not a gruesome look.

```html
<!DOCTYPE html>
<html lang="en">
<head>
<meta charset="utf-8">
<title>Cousin Marigold — Poster</title>
<link rel="stylesheet" href="https://fonts.googleapis.com/css2?family=Bebas+Neue&family=Oswald:wght@400;500;600&family=Saira+Extra+Condensed:wght@600&display=swap">
<style>
  :root {
    --paper: #f7f7f6;
    --title-red: #9c3d48;
    --ink: #2b2b2b;
    --heart-deep: #5e2428;
    --heart-mid: #8a8a88;
    --heart-light: #bdbdbb;
  }
  * { margin: 0; padding: 0; box-sizing: border-box; }
  html, body {
    width: 960px;
    height: 1200px;
    overflow: hidden;
    background: var(--paper);
  }
  .poster {
    position: relative;
    width: 960px;
    height: 1200px;
    background: var(--paper);
  }
  .tagline {
    position: absolute;
    top: 118px;
    left: 0;
    width: 100%;
    text-align: center;
    font-family: "Saira Extra Condensed", "Oswald", sans-serif;
    font-weight: 600;
    font-size: 34px;
    letter-spacing: 0.02em;
    text-transform: uppercase;
    color: var(--ink);
  }
  .key-art {
    position: absolute;
    top: 170px;
    left: 270px;
    width: 420px;
    height: 520px;
  }
  .title {
    position: absolute;
    top: 700px;
    left: 0;
    width: 960px;
    height: 340px;
  }
  .title text {
    font-family: "Bebas Neue", sans-serif;
    font-size: 190px;
    fill: var(--title-red);
  }
  .director {
    position: absolute;
    top: 1048px;
    left: 0;
    width: 100%;
    text-align: center;
    font-family: "Oswald", sans-serif;
    color: var(--title-red);
    text-transform: uppercase;
  }
  .director .lead { font-size: 11px; font-weight: 500; letter-spacing: 0.04em; margin-right: 4px; }
  .director .name { font-size: 22px; font-weight: 500; letter-spacing: 0.02em; }
  .billing {
    position: absolute;
    top: 1084px;
    left: 0;
    width: 100%;
    font-family: "Oswald", sans-serif;
    color: var(--title-red);
    text-transform: uppercase;
    text-align: center;
  }
  .billing-row {
    display: flex;
    justify-content: center;
    align-items: center;
    gap: 10px;
    margin-bottom: 4px;
  }
  .credit { display: inline-flex; align-items: center; gap: 3px; }
  .credit .role {
    font-size: 6px;
    line-height: 1;
    width: 36px;
    text-align: right;
    font-weight: 400;
  }
  .credit .person { font-size: 15px; font-weight: 500; }
</style>
</head>
<body>
<main class="poster">
  <p class="tagline">Turning a blind eye into broken hearts</p>

  <svg class="key-art" viewBox="0 0 100 100" preserveAspectRatio="none" role="img"
       aria-label="Heart frame made of rusted chain, pierced by an arrow, holding a black and white family photograph of a sister and younger brother">
    <defs>
      <linearGradient id="photoTone" x1="0" y1="0" x2="1" y2="1">
        <stop offset="0" stop-color="var(--heart-light)"/>
        <stop offset="1" stop-color="var(--heart-mid)"/>
      </linearGradient>
    </defs>
    <path d="M50 96 C20 72 2 52 2 28 C2 12 14 2 28 2 C38 2 46 8 50 18 C54 8 62 2 72 2 C86 2 98 12 98 28 C98 52 80 72 50 96 Z"
          fill="var(--heart-deep)"/>
    <path d="M50 86 C25 66 9 50 9 29 C9 16 18 9 29 9 C38 9 45 15 50 25 C55 15 62 9 71 9 C82 9 91 16 91 29 C91 50 75 66 50 86 Z"
          fill="url(#photoTone)"/>
  </svg>

  <svg class="title" viewBox="0 0 960 340">
    <defs>
      <filter id="rough">
        <feTurbulence type="fractalNoise" baseFrequency="0.9" numOctaves="2" seed="4" result="noise"/>
        <feColorMatrix in="noise" type="matrix"
          values="0 0 0 0 0  0 0 0 0 0  0 0 0 0 0  0 0 0 -2.2 1.7" result="holes"/>
        <feComposite in="SourceGraphic" in2="holes" operator="in"/>
      </filter>
    </defs>
    <g filter="url(#rough)">
      <text x="480" y="160" text-anchor="middle" textLength="330" lengthAdjust="spacingAndGlyphs">COUSIN</text>
      <text x="480" y="330" text-anchor="middle" textLength="390" lengthAdjust="spacingAndGlyphs">MARIGOLD</text>
    </g>
  </svg>

  <p class="director"><span class="lead">A film by</span><span class="name">Gus Pellam</span></p>

  <div class="billing">
    <div class="billing-row">
      <span class="credit"><span class="role">Costume designer</span><span class="person">Designers Name</span></span>
      <span class="credit"><span class="role">Art director</span><span class="person">Directors Name</span></span>
      <span class="credit"><span class="role">Executive producer</span><span class="person">Producers Name</span></span>
      <span class="credit"><span class="role">Written by</span><span class="person">Writer</span></span>
      <span class="credit"><span class="role">Production designer</span><span class="person">Designers Name</span></span>
    </div>
    <div class="billing-row">
      <span class="credit"><span class="role">Music by</span><span class="person">Musician</span></span>
      <span class="credit"><span class="role">Edited by</span><span class="person">Animator Name</span></span>
      <span class="credit"><span class="role">Director of photography</span><span class="person">Photographers Name</span></span>
    </div>
  </div>
</main>
</body>
</html>
```